'Brantley Electrical' web design

I need a web design for an electrical/electrician company based in sydney called brantley electrical. The logo design and business card design have been uploaded to be used on the web design. I want the design to be very modern and clean. I want the sector designs on the business card, i.e "residential", "commercial" etc, to be fleshed out on the front page. Base those sector designs off the business card but try to make them more minimal and modern to suit the website. Contact details are also on the business card. Try to suit the colour scheme of the logo. The sector designs should be up the top and linked so when clicked it will scroll down the website to brief descriptions of the work the company does in those sectors. I want the website to mainly attract builders, insurance companies and the commercial sector. I want the website to look unique. Custom graphics would be nice to make the website standout. I don't want the website to look like generic.

Target Market(s)

Builders, commercial sector, home owners

Industry/Entity Type

Electrical/Construction

Coding

Coded - Design and coding required

Number of Pages Required

3 page

Requirements
Must have
• Modern design
Nice to have
• Custom graphics that make the website unique

```html
<!DOCTYPE html>
<html lang="en">
<head>
<meta charset="utf-8">
<title>Brantley Electrical</title>
<link href="https://fonts.googleapis.com/css2?family=Montserrat:wght@400;500;600;700&family=Inter:wght@400;500&display=swap" rel="stylesheet">
<style>
:root{
  --navy:#030a24;
  --blue:#0d4fa0;
  --footer-blue:#0f5cad;
  --orange:#f7a032;
  --ink:#1c1c1c;
  --soft:#f7f7f7;
  --white:#ffffff;
  --yellow:#ffe000;
}
*{margin:0;padding:0;box-sizing:border-box}
html,body{width:1200px;height:3820px;overflow:hidden}
body{position:relative;background:var(--white);font-family:"Montserrat",sans-serif;color:var(--ink)}
.abs{position:absolute}

/* hero */
.hero{left:0;top:0;width:1200px;height:618px;background:linear-gradient(180deg,#02061a 0%,#041140 35%,#0b3c7a 60%,#1a5f9a 80%,#0d2f55 100%)}
.skyline{left:0;top:290px;width:1200px;height:328px;background:linear-gradient(180deg,#1b5a8c 0%,#123f6b 50%,#0a2744 100%);opacity:.85}
.brand{left:86px;top:36px;display:flex;align-items:center;gap:10px;color:var(--orange);font-weight:700;font-size:19px;letter-spacing:.2px}
.brand-mark{width:30px;height:30px;background:var(--orange)}
.nav{left:415px;top:42px;display:flex;gap:24px;font-family:"Inter",sans-serif;font-size:14px;color:var(--white)}
.nav-cta{left:890px;top:38px;width:106px;height:30px;background:var(--orange);color:var(--white);border-radius:5px;font-size:11px;font-weight:600;display:flex;align-items:center;justify-content:center}
.nav-phone{left:1018px;top:44px;display:flex;align-items:center;gap:8px;color:var(--white);font-family:"Inter",sans-serif;font-weight:500;font-size:15px}
.nav-rule{left:86px;top:89px;width:1044px;height:1px;background:rgba(255,255,255,.35)}
.hero-title{left:0;top:234px;width:1200px;text-align:center;color:var(--white);font-weight:600;font-size:48px}
.hero-sub{left:0;top:300px;width:1200px;text-align:center;color:var(--white);font-family:"Inter",sans-serif;font-size:19px}
.hero-btn{left:537px;top:347px;width:124px;height:34px;background:var(--orange);color:var(--white);font-size:11px;font-weight:500;display:flex;align-items:center;justify-content:center;gap:8px}

/* about */
.about{left:0;top:618px;width:1200px;height:342px;background:var(--soft)}
.about-icon{left:109px;top:680px}
.about-label{left:117px;top:742px;font-size:19px;color:#333}
.about-heading{left:112px;top:778px;font-size:34px;font-weight:600;line-height:42px}
.about-heading .accent{color:var(--orange)}
.about-text{left:628px;top:702px;width:490px;font-family:"Inter",sans-serif;font-size:13px;line-height:27.5px;color:#111}

/* sectors */
.photo{display:block}
.panel{background:var(--white)}
.sector-title{font-size:29px;font-weight:600;color:var(--ink)}
.sector-text{width:420px;font-size:17px;line-height:28.5px;color:#222}
.btn-blue{background:var(--blue);color:var(--white);font-size:13px;font-weight:600;display:flex;align-items:center;justify-content:center}
.btn-orange{background:var(--orange);color:var(--white);font-size:11px;font-weight:500;display:flex;align-items:center;justify-content:center}

/* quote */
.quote-title{left:162px;top:3170px;font-size:42px;font-weight:500}
.field-label{font-size:17px;font-weight:500;color:#222}
.field-line{height:1px;width:358px;background:#444;left:166px}
.send{left:168px;top:3579px;width:81px;height:34px}
.to-top{left:1008px;top:3531px;width:54px;height:54px;border-radius:50%;background:var(--yellow);display:flex;align-items:center;justify-content:center}
.to-top-label{left:995px;top:3588px;width:80px;text-align:center;font-size:12px;color:var(--white)}

/* footer */
.footer{left:0;top:3577px;width:1200px;height:243px;background:linear-gradient(90deg,#0b55a6,#1467b7)}
.footer-col{color:var(--white);font-size:14px;line-height:22px}
.footer-col strong{font-weight:600}
.socials{left:924px;top:3670px;display:flex;gap:13px}
.social{width:20px;height:20px;border-radius:50%;background:var(--white)}
.copyright{left:111px;top:3712px;font-size:11px;color:#333}
</style>
</head>
<body>

<!-- hero -->
<div class="abs hero"></div>
<div class="abs skyline" role="img" aria-label="Night city skyline with lit office towers"></div>
<div class="abs brand"><span class="brand-mark"></span>Brantley Electrical</div>
<nav class="abs nav"><span>About us</span><span>Commercial</span><span>Construction</span><span>Industrial</span><span>Residential</span></nav>
<div class="abs nav-cta">CONTACT US</div>
<div class="abs nav-phone">
  <svg width="18" height="18" viewBox="0 0 24 24" fill="none" stroke="#fff" stroke-width="1.8"><path d="M5 3h4l2 5-2.5 1.5a11 11 0 0 0 6 6L16 13l5 2v4a2 2 0 0 1-2 2A16 16 0 0 1 3 5a2 2 0 0 1 2-2z"/></svg>
  0412 555 019
</div>
<div class="abs nav-rule"></div>
<h1 class="abs hero-title">Welcome to Brantley Electrical</h1>
<p class="abs hero-sub">Powering Your Projects</p>
<div class="abs hero-btn">Get In Touch
  <svg width="12" height="10" viewBox="0 0 12 10" fill="none" stroke="#fff" stroke-width="1.4"><path d="M0 5h10M6 1l4 4-4 4"/></svg>
</div>

<!-- about -->
<section class="abs about"></section>
<svg class="abs about-icon" width="40" height="40" viewBox="0 0 40 40"><circle cx="20" cy="20" r="18" fill="none" stroke="#0d4fa0" stroke-width="2.5"/><path d="M22 9l-9 13h6l-2 9 9-13h-6z" fill="#0d4fa0"/></svg>
<div class="abs about-label">About us</div>
<h2 class="abs about-heading"><span class="accent">Your Reliable Electrical</span><br>Service in Sydney</h2>
<p class="abs about-text">Lorem ipsum dolor sit amet, consectetur adipiscing elit. Tellus nunc amet adipiscing tellus, vitae. Malesuada quam volutpat maecenas lectus eu. Et pellentesque mattis in in magna et. Pharetra nunc egestas dictum rhoncus ac elit vestibulum. Metus, et nunc imperdiet id felis vitae pretium hac. Pulvinar mauris, massa vitae faucibus ipsum felis. Placerat velit tempus ullamcorper blandit. Nunc lacus maecenas arcu, consequat id feugiat amet, cursus mollis.</p>

<!-- commercial -->
<div class="abs photo" style="left:406px;top:960px;width:794px;height:558px;background:linear-gradient(120deg,#8e8a84,#c9c6c0 45%,#6f7478)" role="img" aria-label="Electrician in a hard hat checking a switchboard with a tablet"></div>
<div class="abs panel" style="left:0;top:1019px;width:571px;height:439px"></div>
<h3 class="abs sector-title" style="left:101px;top:1114px">Commercial</h3>
<p class="abs sector-text" style="left:101px;top:1162px">Lorem ipsum dolor sit amet consectetur. Phasellus nullam cras eu sit fermentum faucibus velit. Eu integer commodo facilisis a adipiscing tristique sed magnis et. Sed sit augue vehicula amet nibh lectus vitae. Id aliquet malesuada sed tincidunt nec ut. Nunc cras elementum nibh.</p>
<div class="abs btn-blue" style="left:105px;top:1375px;width:150px;height:40px">Contact us today!</div>

<!-- construction -->
<div class="abs photo" style="left:0;top:1585px;width:558px;height:392px;background:linear-gradient(180deg,#b8a69a 0%,#e0b48a 45%,#7a5b48 75%,#3b2d26 100%)" role="img" aria-label="Two workers on a construction site with a tower crane at sunset"></div>
<h3 class="abs sector-title" style="left:657px;top:1618px">Construction</h3>
<p class="abs sector-text" style="left:657px;top:1667px">Lorem ipsum dolor sit amet consectetur. Phasellus nullam cras eu sit fermentum faucibus velit. Eu integer commodo facilisis a adipiscing tristique sed magnis et. Sed sit augue vehicula amet nibh lectus vitae. Id aliquet malesuada sed tincidunt nec ut. Nunc cras elementum nibh.</p>
<div class="abs btn-orange" style="left:661px;top:1864px;width:127px;height:34px">Get In Touch</div>

<!-- industrial -->
<div class="abs photo" style="left:409px;top:2012px;width:791px;height:558px;background:linear-gradient(170deg,#5b6a85 0%,#d98a55 40%,#6b4a40 65%,#2a2426 100%)" role="img" aria-label="Industrial plant with chimneys under an orange sunset sky"></div>
<div class="abs panel" style="left:0;top:2072px;width:599px;height:439px"></div>
<h3 class="abs sector-title" style="left:130px;top:2166px">Industrial</h3>
<p class="abs sector-text" style="left:130px;top:2214px">Lorem ipsum dolor sit amet consectetur. Phasellus nullam cras eu sit fermentum faucibus velit. Eu integer commodo facilisis a adipiscing tristique sed magnis et. Sed sit augue vehicula amet nibh lectus vitae. Id aliquet malesuada sed tincidunt nec ut. Nunc cras elementum nibh.</p>
<div class="abs btn-blue" style="left:135px;top:2426px;width:148px;height:42px">Contact us today!</div>

<!-- residential -->
<div class="abs photo" style="left:0;top:2637px;width:570px;height:393px;background:linear-gradient(100deg,#3a3a3e 0%,#8c8b8a 45%,#5e544c 75%,#2f2a27 100%)" role="img" aria-label="Electrician in a hard hat wiring a home circuit board"></div>
<h3 class="abs sector-title" style="left:669px;top:2671px">Residential</h3>
<p class="abs sector-text" style="left:669px;top:2720px">Lorem ipsum dolor sit amet consectetur. Phasellus nullam cras eu sit fermentum faucibus velit. Eu integer commodo facilisis a adipiscing tristique sed magnis et. Sed sit augue vehicula amet nibh lectus vitae. Id aliquet malesuada sed tincidunt nec ut. Nunc cras elementum nibh.</p>
<div class="abs btn-orange" style="left:661px;top:2927px;width:127px;height:35px">Get In Touch</div>

<!-- quote -->
<div class="abs photo" style="left:584px;top:3030px;width:616px;height:547px;background:linear-gradient(135deg,#3e3226 0%,#7a5a36 40%,#2c2620 70%,#4a3c30 100%)" role="img" aria-label="Blurred close-up of a technician testing wiring with a multimeter"></div>
<div class="abs footer"></div>
<div class="abs panel" style="left:111px;top:3030px;width:473px;height:652px"></div>
<h2 class="abs quote-title">Request a Quote</h2>
<div class="abs field-label" style="left:166px;top:3243px">Name*</div>
<div class="abs field-line" style="top:3281px"></div>
<div class="abs field-label" style="left:166px;top:3301px">Email*</div>
<div class="abs field-line" style="top:3338px"></div>
<div class="abs field-label" style="left:166px;top:3361px">Phone number</div>
<div class="abs field-line" style="top:3399px"></div>
<div class="abs field-label" style="left:166px;top:3434px">Message</div>
<div class="abs field-line" style="top:3505px"></div>
<div class="abs btn-blue send">Send</div>

<div class="abs to-top">
  <svg width="20" height="20" viewBox="0 0 20 20" fill="none" stroke="#222" stroke-width="1.6"><path d="M10 17V3M4 9l6-6 6 6"/></svg>
</div>
<div class="abs to-top-label">back to top</div>

<!-- footer -->
<div class="abs footer-col" style="left:639px;top:3640px"><strong>Brantley Electrical</strong><br>27 Harbour Lane<br>Marrickville, 2204</div>
<div class="abs footer-col" style="left:639px;top:3720px">hello@brantleyelectrical.example</div>
<div class="abs footer-col" style="left:639px;top:3753px">+0412555019</div>
<div class="abs footer-col" style="left:922px;top:3640px"><strong>Connect with us</strong></div>
<div class="abs socials"><span class="social"></span><span class="social"></span><span class="social"></span><span class="social"></span></div>
<div class="abs copyright">Copyright © 2022 Brantley Electrical. All Rights Reserved.</div>

</body>
</html>
```